Quillory Points website re-design and

the institute of massage therapy is ready for a new website. The current website is around 12 years old and it looks old. Luckily the clients is not against changing the colors so the new design does not have to use the current ugly green color scheme. Be creative! Make it pretty, modern and inviting. The current colors look like mold. Nobody likes mold. I have attached the logo asset file as well as a txt document that details the new website design parameters

1 page

```html
<!DOCTYPE html>
<html lang="en">
<head>
<meta charset="utf-8">
<title>Institute of Tidewell Therapy</title>
<link href="https://fonts.googleapis.com/css2?family=Playfair+Display:wght@400;500;700&family=Poppins:wght@300;400;500;600;700&display=swap" rel="stylesheet">
<style>
:root{
  --blue:#1a8fd8;
  --blue-dark:#0f6fb0;
  --teal-deep:#0c3342;
  --teal:#145064;
  --ink:#1d2b36;
  --text:#55606a;
  --light:#f1f3f5;
  --footer:#1a222c;
  --yellow:#f5d020;
  --white:#ffffff;
}
*{box-sizing:border-box;margin:0;padding:0}
html,body{width:1200px;height:3544px;overflow:hidden}
body{font-family:"Poppins",sans-serif;color:var(--text);background:var(--white);position:relative}
.btn{display:inline-flex;align-items:center;gap:10px;background:var(--blue);color:var(--white);font-size:14px;font-weight:500;padding:0 6px 0 20px;height:36px;border-radius:18px}
.btn .dot{width:26px;height:26px;border-radius:50%;background:var(--white);display:flex;align-items:center;justify-content:center}
.abs{position:absolute}

/* top bar */
.topbar{top:0;left:0;width:1200px;height:32px;background:var(--white);border-bottom:1px solid #e6e9ec}
.topbar .socials{left:120px;top:9px;display:flex;gap:12px}
.topbar .socials span{width:14px;height:14px;border-radius:3px;background:var(--blue)}
.topbar .links{right:120px;top:7px;font-size:12px;color:var(--ink)}

/* header */
.header{top:32px;left:0;width:1200px;height:80px;background:var(--white)}
.brand{display:flex;align-items:center;gap:12px}
.brand .mark{width:30px;height:30px;border-radius:50%;background:var(--teal)}
.brand .name{font-size:16px;font-weight:600;color:var(--ink);line-height:1.1;width:150px}
.header .brand{left:120px;top:20px}
.nav{right:120px;top:22px;display:flex;align-items:center;gap:8px;font-size:13px;font-weight:500;color:var(--ink)}
.nav a{padding:9px 16px;color:var(--ink);text-decoration:none}
.nav a.active{background:var(--blue);color:var(--white)}
.nav a.login{background:var(--blue);color:var(--white);border-radius:18px;padding:8px 22px;margin-left:10px}

/* hero */
.hero{top:112px;left:0;width:1200px;height:420px;background:linear-gradient(100deg,#0a2c3a 0%,#154b5c 55%,#0d3646 100%);overflow:hidden}
.hero-art{left:760px;top:20px;width:250px;height:330px;background:linear-gradient(160deg,#d9b9a4,#8e6a58 55%,#3b2a24);border-radius:6px;opacity:.9}
.hero-copy{left:140px;top:135px;color:var(--white)}
.hero-copy .kicker{font-size:22px;font-weight:400}
.hero-copy h1{font-family:"Playfair Display",serif;font-weight:500;font-size:44px;line-height:1.2;margin-top:6px}
.hero-copy .btn{margin-top:26px}
.hero-wave{left:0;bottom:0}

/* about */
.about-photo{left:0;top:560px;width:540px;height:360px;background:linear-gradient(120deg,#e9dcd0,#c8a68d 50%,#8a6a55)}
.about-bar{left:0;top:925px;width:110px;height:32px;background:var(--blue)}
.about-copy{left:600px;top:610px;width:500px;color:var(--ink)}
.about-copy .kicker{font-size:24px}
.about-copy h2{font-family:"Playfair Display",serif;font-weight:500;font-size:44px;line-height:1.1}
.about-copy p{font-size:14px;line-height:1.75;color:var(--text);margin-top:26px}
.about-copy .btn{margin-top:24px}

/* free course band */
.freeband{top:992px;left:0;width:1200px;height:388px;background:linear-gradient(90deg,#2b2b2b 0%,#5a5a5a 45%,#3a3a3a 100%)}
.freeband-copy{left:130px;top:1062px;color:var(--white)}
.freeband-copy h2{font-family:"Playfair Display",serif;font-weight:400;font-size:72px;line-height:1.05}
.freeband-copy p{font-size:22px;font-weight:600;margin-top:20px;line-height:1.3}
.freeband-copy p em{font-style:normal;color:var(--yellow)}

/* popular courses */
.section-title{left:0;width:1200px;text-align:center;color:var(--ink)}
.section-title .kicker{font-size:22px}
.section-title h2{font-family:"Playfair Display",serif;font-weight:700;font-size:46px;line-height:1.15}
.course{top:1552px;width:300px;text-align:center}
.course .arch{width:300px;height:270px;border-radius:150px 150px 0 0}
.course h3{font-family:"Playfair Display",serif;font-weight:500;font-size:22px;color:var(--ink);margin-top:20px}
.course p{font-size:13px;line-height:1.6;margin:10px 14px 0;height:64px}
.course .btn{margin-top:18px}

/* why choose us */
.why{top:2100px;left:0;width:1200px;height:540px;background:var(--light)}
.why-sub{left:0;top:2210px;width:1200px;text-align:center;font-size:14px;color:var(--ink)}
.card{top:2270px;width:240px;height:290px;background:var(--white);border-radius:8px;box-shadow:0 6px 18px rgba(0,0,0,.06)}
.card .panel{position:absolute;left:12px;top:-10px;width:216px;height:200px;border-radius:12px;padding:22px 22px;color:var(--white)}
.card .icon{width:40px;height:40px;border-radius:8px;background:rgba(255,255,255,.22);display:flex;align-items:center;justify-content:center}
.card .panel p{font-size:11.5px;line-height:1.55;margin-top:12px}
.card .panel .more{font-size:10px;font-weight:600;margin-top:8px;letter-spacing:.5px}
.card .meta{position:absolute;left:22px;top:214px;display:flex;gap:10px;align-items:center}
.card .num{font-size:30px;font-weight:600;color:var(--blue)}
.card .label{font-family:"Playfair Display",serif;font-size:15px;color:var(--ink);line-height:1.2;width:140px}

/* contact */
.contact{top:2640px;left:0;width:1200px;height:460px;background:linear-gradient(110deg,#0a2a36,#12495a 60%,#0c3242)}
.contact-title{left:0;top:2730px;width:1200px;text-align:center;font-family:"Playfair Display",serif;font-weight:700;font-size:44px;line-height:1.2;color:var(--white)}
.field{height:30px;background:var(--white);font-size:11px;color:#8b939a;padding:8px 12px}
.submit{left:540px;top:3040px;width:120px;height:30px;border-radius:15px;background:var(--blue);color:var(--white);font-size:12px;font-weight:600;display:flex;align-items:center;justify-content:center}

/* footer */
.footer{top:3100px;left:0;width:1200px;height:444px;background:var(--footer)}
.footer-brand{left:130px;top:3190px}
.footer-brand .mark{background:var(--blue)}
.footer-brand .name{color:var(--white)}
.footer-socials{left:130px;top:3250px;display:flex;gap:10px}
.footer-socials span{width:28px;height:28px;border-radius:50%;background:var(--blue)}
.fcol{top:3200px;font-size:13px;line-height:2;color:#c9d0d6}
.fcol h4{font-family:"Playfair Display",serif;font-size:18px;font-weight:500;color:var(--blue);margin-bottom:10px}
.vline{top:3190px;width:1px;height:210px;background:#3a4450}
.contact-row{display:flex;gap:10px;align-items:flex-start;line-height:1.5;margin-bottom:14px}
.contact-row .ic{flex:none;width:22px;height:22px;border-radius:50%;background:var(--blue);display:flex;align-items:center;justify-content:center}
.copyright{left:0;top:3500px;width:1200px;text-align:center;font-size:11px;color:#9aa4ad}
.copyright b{color:var(--blue);font-weight:500}
</style>
</head>
<body>

<div class="abs topbar">
  <div class="abs socials"><span></span><span></span><span></span><span></span></div>
  <div class="abs links">Contact Us &nbsp;|&nbsp; About Us &nbsp;|&nbsp; Policies</div>
</div>

<header class="abs header">
  <div class="abs brand"><span class="mark"></span><span class="name">Institute of Tidewell Therapy</span></div>
  <nav class="abs nav">
    <a class="active">HOME</a><a>COURSES</a><a>PACKAGES</a><a>SUBSIDIARIES</a><a>FAQ</a><a class="login">LOGIN</a>
  </nav>
</header>

<section class="abs hero" role="img" aria-label="Dark teal photo of a massage therapy session">
  <div class="abs hero-art" role="img" aria-label="Photo of a therapist's hands along a spine"></div>
  <div class="abs hero-copy">
    <div class="kicker">Committed to Excellence in</div>
    <h1>Massage Therapy<br>Continuing Education</h1>
    <span class="btn">Contact Us <span class="dot"><svg width="10" height="10" viewBox="0 0 10 10"><path d="M3 1l4 4-4 4" stroke="#1a8fd8" stroke-width="2" fill="none"/></svg></span></span>
  </div>
  <svg class="abs hero-wave" width="1200" height="80" viewBox="0 0 1200 80">
    <path d="M0 60 C300 10 700 90 1200 20 L1200 80 L0 80Z" fill="#ffffff"/>
    <path d="M0 58 C300 8 700 88 1200 18" stroke="#1a8fd8" stroke-width="4" fill="none"/>
  </svg>
</section>

<div class="abs about-photo" role="img" aria-label="Photo of a woman receiving a back massage"></div>
<div class="abs about-bar"></div>
<div class="abs about-copy">
  <div class="kicker">The Institute of</div>
  <h2>Tidewell Therapy</h2>
  <p>The Institute of Tidewell Therapy is committed to providing the best online home study continuing education courses available to massage therapists. Institute of Tidewell Therapy is approved by the National Council for Bodywork Education (NCBE) as a continuing education Approved Provider.</p>
  <span class="btn">Read More <span class="dot"><svg width="10" height="10" viewBox="0 0 10 10"><path d="M3 1l4 4-4 4" stroke="#1a8fd8" stroke-width="2" fill="none"/></svg></span></span>
</div>

<section class="abs freeband" role="img" aria-label="Grayscale photo of hands massaging a shoulder"></section>
<div class="abs freeband-copy">
  <h2>Take<br>Free Course</h2>
  <p>Click here to get started today &amp;<br>try our <em>FREE online course!</em></p>
</div>

<div class="abs section-title" style="top:1450px">
  <div class="kicker">Our Most</div>
  <h2>Popular Courses</h2>
</div>

<div class="abs course" style="left:132px">
  <div class="arch" role="img" aria-label="Photo of a pregnant woman" style="background:linear-gradient(160deg,#e8c9ae,#b98567 60%,#7a5442)"></div>
  <h3>Pregnancy / Doula</h3>
  <p>Courses and packages to become certified in every stage of childbearing, from infertility to infant massage.</p>
  <span class="btn">Read More <span class="dot"><svg width="10" height="10" viewBox="0 0 10 10"><path d="M3 1l4 4-4 4" stroke="#1a8fd8" stroke-width="2" fill="none"/></svg></span></span>
</div>
<div class="abs course" style="left:452px">
  <div class="arch" role="img" aria-label="Institute badge" style="background:#2f5a46"></div>
  <h3>Florida Laws &amp; Packages</h3>
  <p>Courses and packages required to obtain, reinstate, or renew your Florida massage therapy license.</p>
  <span class="btn">Read More <span class="dot"><svg width="10" height="10" viewBox="0 0 10 10"><path d="M3 1l4 4-4 4" stroke="#1a8fd8" stroke-width="2" fill="none"/></svg></span></span>
</div>
<div class="abs course" style="left:772px">
  <div class="arch" role="img" aria-label="Photo of a woman studying at a laptop" style="background:linear-gradient(160deg,#f3ece6,#d9b7a3 55%,#b97b6a)"></div>
  <h3>Research Courses</h3>
  <p>Courses approved by the NCBE to earn mandated research hours for Board Certification renewal.</p>
  <span class="btn">Read More <span class="dot"><svg width="10" height="10" viewBox="0 0 10 10"><path d="M3 1l4 4-4 4" stroke="#1a8fd8" stroke-width="2" fill="none"/></svg></span></span>
</div>

<section class="abs why"></section>
<div class="abs section-title" style="top:2140px"><h2>Why Choose Us</h2></div>
<div class="abs why-sub">Three reasons why the institute of tidewell therapy offers The best online continuing education experience</div>

<div class="abs card" style="left:150px">
  <div class="panel" style="background:linear-gradient(150deg,#2aa3e6,#1272b8)">
    <div class="icon"><svg width="20" height="20" viewBox="0 0 20 20"><rect x="4" y="2" width="12" height="16" rx="2" stroke="#fff" stroke-width="2" fill="none"/><path d="M7 7h6M7 11h6" stroke="#fff" stroke-width="2"/></svg></div>
    <p>Simply enroll in any of our online continuing education courses and get your certificate the moment you finish.</p>
    <div class="more">READ MORE</div>
  </div>
  <div class="meta"><span class="num">01</span><span class="label">Instant Access and Results</span></div>
</div>
<div class="abs card" style="left:410px">
  <div class="panel" style="background:linear-gradient(150deg,#22a9d6,#1180a8)">
    <div class="icon"><svg width="20" height="20" viewBox="0 0 20 20"><circle cx="10" cy="10" r="7" stroke="#fff" stroke-width="2" fill="none"/><path d="M6.5 10l2.5 2.5 4.5-5" stroke="#fff" stroke-width="2" fill="none"/></svg></div>
    <p>With our online courses you can study at your own pace. No travel, no fixed schedule, and no waiting rooms.</p>
    <div class="more">READ MORE</div>
  </div>
  <div class="meta"><span class="num">02</span><span class="label">Hassle Free</span></div>
</div>
<div class="abs card" style="left:670px">
  <div class="panel" style="background:linear-gradient(150deg,#1bb3c4,#0f8a99)">
    <div class="icon"><svg width="20" height="20" viewBox="0 0 20 20"><path d="M10 2l7 3v5c0 4-3 7-7 8-4-1-7-4-7-8V5z" stroke="#fff" stroke-width="2" fill="none"/></svg></div>
    <p>Take a free course to see our content first. You pay nothing to try our format and learning style.</p>
    <div class="more">READ MORE</div>
  </div>
  <div class="meta"><span class="num">03</span><span class="label">Risk Free Sample Course</span></div>
</div>
<div class="abs card" style="left:930px">
  <div class="panel" style="background:linear-gradient(150deg,#16b49a,#0e8a74)">
    <div class="icon"><svg width="20" height="20" viewBox="0 0 20 20"><path d="M10 3v14M3 10h14" stroke="#fff" stroke-width="2"/></svg></div>
    <p>Simply enroll in a course that suits you and join therapists who trust our approved home study courses.</p>
    <div class="more">READ MORE</div>
  </div>
  <div class="meta"><span class="num">04</span><span class="label">And 8 More Reasons</span></div>
</div>

<section class="abs contact" role="img" aria-label="Dark teal photo of a massage room"></section>
<h2 class="abs contact-title">Get In Touch With Us</h2>
<div class="abs field" style="left:280px;top:2830px;width:315px">Name</div>
<div class="abs field" style="left:605px;top:2830px;width:315px">Course</div>
<div class="abs field" style="left:280px;top:2870px;width:315px">Email</div>
<div class="abs field" style="left:605px;top:2870px;width:315px">Phone</div>
<div class="abs field" style="left:280px;top:2910px;width:640px;height:110px">Message</div>
<div class="abs submit">SUBMIT</div>

<footer class="abs footer"></footer>
<div class="abs brand footer-brand"><span class="mark"></span><span class="name">Institute of Tidewell Therapy</span></div>
<div class="abs footer-socials"><span></span><span></span><span></span><span></span><span></span></div>
<div class="abs vline" style="left:410px"></div>
<div class="abs fcol" style="left:448px">
  <h4>Quick Links</h4>
  Home<br>About Us<br>Course<br>Package<br>Insurance<br>FAQ<br>Contact Us
</div>
<div class="abs vline" style="left:610px"></div>
<div class="abs fcol" style="left:640px;width:250px">
  <h4>Contacts</h4>
  <div class="contact-row"><span class="ic"><svg width="10" height="12" viewBox="0 0 10 12"><path d="M5 11S1 7 1 4.5a4 4 0 018 0C9 7 5 11 5 11z" fill="#fff"/></svg></span><span>2150 Harbor Palm Avenue,<br>Tampa FL 33601</span></div>
  <div class="contact-row"><span class="ic"><svg width="10" height="10" viewBox="0 0 10 10"><path d="M2 1l2 2-1 1.5 2.5 2.5L7 6l2 2-1.5 1.5C4 9 1 6 .5 2.5z" fill="#fff"/></svg></span><span>(813) 555-0142</span></div>
  <div class="contact-row"><span class="ic"><svg width="10" height="8" viewBox="0 0 10 8"><rect x=".5" y=".5" width="9" height="7" stroke="#fff" fill="none"/><path d="M.5 .5l4.5 4 4.5-4" stroke="#fff" fill="none"/></svg></span><span>hello@tidewelltherapy.example</span></div>
</div>
<div class="abs vline" style="left:900px"></div>
<div class="abs fcol" style="left:928px">
  <h4>Courses</h4>
  Pregnancy / Doula<br>Florida Laws &amp; Packages<br>Research Courses
</div>
<div class="abs copyright">Copyright © 2023 <b>Institute of Tidewell Therapy</b>. All Rights Reserved.</div>

</body>
</html>
```